Style with Kindness needs a new flyer fast for a giveaway

I am running a contest for the month of December. The woman selected as the winner of the contest will be someone that that has survived a domestic violence situation but would like to kick start in her new life journey. The winner selected will receive 1 month free personal training with a fitness coach 3 times a week, 4 week delivery of smoothies from Leafwhirler and a style consultation and outfit by Celebrity Stylist R.Tasker. All interested candidates should submit a brief personal bio including the reason they should be selected. Submissions are due December 24th and the winner will be selected December 31. Submissions should be sent to stylewithkindnessdallas@mailbox-example.net

Industry/Entity Type

Fashion

Font styles to use
Serif

Colors
886aae
b7a5cd
e4daeb
d2a4cc
b768aa
a64599
e34197
e667a6
eea4c8

Requirements
Must have
• The project has to be worded in a stylish way. I want it is be creative and eye catchy. It also needs to have my style with kindness logo and my Ava P logo on the flyer that I will attach to the brief
Nice to have
• I would like to see different fonts to break up the flyer
Should not have
• It should not just be a paragraph of what I already typed about the contest

```html
<!DOCTYPE html>
<html lang="en">
<head>
<meta charset="utf-8">
<title>Celebration of Survivors – Style with Kindness</title>
<link rel="stylesheet" href="https://fonts.googleapis.com/css2?family=PT+Sans:ital,wght@0,400;0,700;1,700&family=PT+Sans+Narrow:wght@400;700&display=swap">
<style>
  :root {
    --violet-deep: #4a2f6e;
    --violet: #6b4796;
    --violet-band: #6d4aa0;
    --violet-mid: #886aae;
    --lavender: #b7a5cd;
    --lavender-pale: #ddd0e8;
    --lavender-box: #d9cce6;
    --rose: #b768aa;
    --pink: #e34197;
    --ink: #1d1424;
    --white: #ffffff;
  }
  * { margin: 0; padding: 0; box-sizing: border-box; }
  html, body { width: 934px; height: 1200px; overflow: hidden; }
  body { font-family: "PT Sans", sans-serif; background: var(--violet); }

  .flyer { position: relative; width: 934px; height: 1200px; overflow: hidden; }

  .hero-photo {
    position: absolute; inset: 0;
    background:
      radial-gradient(ellipse 320px 420px at 720px 330px, rgba(225,190,200,0.55), transparent 70%),
      radial-gradient(ellipse 260px 360px at 300px 300px, rgba(200,190,215,0.45), transparent 70%),
      radial-gradient(ellipse 260px 200px at 760px 640px, rgba(190,70,130,0.45), transparent 70%),
      linear-gradient(160deg, #7c6a97 0%, #8f7aae 30%, #7a5a9e 55%, #6a4896 75%, #5e3f8c 100%);
  }

  .headline {
    position: absolute; left: 54px; top: 382px;
    font-family: "PT Sans Narrow", sans-serif; font-weight: 700;
    color: var(--white); line-height: 0.92;
    text-shadow: 0 2px 6px rgba(0,0,0,0.35);
  }
  .headline .line-small { font-size: 57px; display: block; }
  .headline .line-small .light { font-weight: 400; }
  .headline .line-large { font-size: 82px; display: block; }

  .question-band {
    position: absolute; left: 0; top: 546px; width: 934px; height: 68px;
    background: var(--violet-band);
    display: flex; align-items: center; padding-left: 56px;
  }
  .question-band h2 {
    font-family: "PT Sans Narrow", sans-serif; font-weight: 700;
    font-size: 33px; color: var(--white); letter-spacing: 0.2px;
  }

  .intro {
    position: absolute; left: 56px; top: 638px;
    font-family: "PT Sans Narrow", sans-serif; font-weight: 700;
    color: var(--white); line-height: 1.5;
  }
  .intro .first { font-size: 23px; display: block; }
  .intro .second { font-size: 26px; display: block; line-height: 1.3; }

  .prize-card {
    position: absolute; left: 38px; top: 718px; width: 460px; height: 280px;
    background: var(--lavender-box);
    border-radius: 22px 22px 0 0;
    padding: 22px 28px 0 28px;
  }
  .prize-card h3 {
    font-weight: 400; font-size: 24px; color: var(--ink);
    padding-bottom: 14px; margin-bottom: 14px;
    background: linear-gradient(90deg, transparent, #888 20%, #888 60%, transparent) bottom / 100% 1px no-repeat;
  }
  .prize-list { list-style: none; }
  .prize-list li {
    position: relative; padding-left: 34px; margin-bottom: 10px;
    font-weight: 700; font-style: italic; font-size: 19.5px; line-height: 1.3; color: var(--ink);
  }
  .prize-list svg { position: absolute; left: 0; top: 6px; }

  .brand-strip {
    position: absolute; left: 38px; top: 998px; width: 460px; height: 124px;
    background: linear-gradient(180deg, var(--lavender-pale) 70%, rgba(221,208,232,0.6));
    display: flex; align-items: center;
  }
  .brand-name {
    font-weight: 400; font-size: 24px; color: var(--violet);
    width: 220px; text-align: center; line-height: 1.1;
  }
  .brand-divider { width: 1px; height: 78px; background: var(--lavender); }

  .submit-note {
    position: absolute; left: 536px; top: 760px; width: 330px;
    font-family: "PT Sans Narrow", sans-serif; font-weight: 700;
    font-size: 19px; line-height: 1.38; color: var(--ink);
  }
  .deadline {
    position: absolute; left: 536px; top: 868px; width: 360px;
    color: var(--ink); line-height: 1.3;
  }
  .deadline .lead { font-size: 20px; display: block; }
  .deadline .date {
    font-family: "PT Sans Narrow", sans-serif; font-weight: 700; font-size: 27px;
  }
  .deadline .join {
    font-family: "PT Sans Narrow", sans-serif; font-weight: 700; font-size: 19px;
  }

  .contact-panel {
    position: absolute; left: 498px; top: 998px; width: 436px; height: 114px;
    background: var(--lavender-box);
    padding: 20px 0 0 34px; color: var(--ink);
  }
  .contact-panel h4 { font-weight: 700; font-size: 31px; letter-spacing: 0.3px; }
  .contact-panel p { font-size: 16px; margin-top: 4px; }
</style>
</head>
<body>
<main class="flyer">
  <div class="hero-photo" role="img" aria-label="Photo of a confident woman in a gym holding a dumbbell towards the camera, with a man training in the blurred background, tinted in purple tones"></div>

  <h1 class="headline">
    <span class="line-small">CELEBRATION <span class="light">OF</span></span>
    <span class="line-large">SURVIVORS</span>
  </h1>

  <div class="question-band">
    <h2>HAVE YOU SURVIVED A DOMESTIC VIOLENCE SITUATION?</h2>
  </div>

  <p class="intro">
    <span class="first">During the month of December,</span>
    <span class="second">enter for the opportunity for us to help kick start your new journey.</span>
  </p>

  <section class="prize-card">
    <h3>The winner selected will receive:</h3>
    <ul class="prize-list">
      <li><svg width="22" height="18" viewBox="0 0 22 18"><path d="M2 10 L8 16 L20 2" fill="none" stroke="#1d1424" stroke-width="3.2" stroke-linecap="round" stroke-linejoin="round"/></svg>1 month FREE personal training with a fitness coach 3 times a week.</li>
      <li><svg width="22" height="18" viewBox="0 0 22 18"><path d="M2 10 L8 16 L20 2" fill="none" stroke="#1d1424" stroke-width="3.2" stroke-linecap="round" stroke-linejoin="round"/></svg>4 week delivery of smoothies from Leafwhirler</li>
      <li><svg width="22" height="18" viewBox="0 0 22 18"><path d="M2 10 L8 16 L20 2" fill="none" stroke="#1d1424" stroke-width="3.2" stroke-linecap="round" stroke-linejoin="round"/></svg>A style consultation by Celebrity Stylist R.Tasker</li>
    </ul>
  </section>

  <div class="brand-strip">
    <span class="brand-name">Style with Kindness</span>
    <span class="brand-divider"></span>
    <span class="brand-name">Ava P</span>
  </div>

  <p class="submit-note">All interested should submit a brief personal bio including the reason you should be selected.</p>

  <p class="deadline">
    <span class="lead">Submissions are due</span>
    <span class="date">December 24th</span> <span class="join">and the winner will be</span><br>
    <span class="date">selected December 31.</span>
  </p>

  <section class="contact-panel">
    <h4>CONTACT US</h4>
    <p>stylewithkindnessdallas@mailbox-example.net</p>
  </section>
</main>
</body>
</html>
```